Design a Book Cover for a Bill Tracker Logbook

We are looking for a designer to create a book cover for a bill tracker. The detailed instructions and interior pages are attached. For those who are new to RVM, the cover template is also attached.
Please be creative and focus on creating a trustworthy, reliable, modern, and secure feeling based on the theme. You are allowed to use downloaded templates, but you must provide commercial licenses.
Attention: We are happy to pay extra tip if you are selected with a really high quality design.
US

```html
<!DOCTYPE html>
<html lang="en">
<head>
<meta charset="utf-8">
<title>Bill Tracker &amp; Password Log – Cover Wrap</title>
<link rel="stylesheet" href="https://fonts.googleapis.com/css2?family=Cinzel:wght@400&family=Lato:wght@400&display=swap">
<style>
:root{
  --cover-blue:#0456ad;
  --ink-white:#ffffff;
  --rule-blue:#5e9be0;
  --author-blue:#a9c4e6;
  --badge-dark:#1c2a3d;
  --page-white:#ffffff;
  --page-grey:#d9dde3;
  --barcode-cyan:#00c3ff;
}
*{margin:0;padding:0;box-sizing:border-box}
html,body{width:1200px;height:772px;overflow:hidden;background:var(--cover-blue)}
.cover{position:relative;width:1200px;height:772px;background:var(--cover-blue);color:var(--ink-white);font-family:"Cinzel",serif}
.abs{position:absolute}
.center-x{transform:translateX(-50%);white-space:nowrap;text-align:center}

.title-line{font-weight:400;line-height:1}
.back .title-line{font-size:31px;letter-spacing:-0.06em}
.front .title-line{font-size:56px;letter-spacing:-0.065em}
.amp{font-weight:400;line-height:1}
.rule{position:absolute;height:2px;background:var(--rule-blue)}
.caps{font-weight:400;font-variant:small-caps}

.feature{font-size:16px;letter-spacing:0.02em}
.thanks{font-size:12.5px;line-height:13.3px;letter-spacing:0.01em}

.page-thumb{position:absolute;width:53px;height:69px;background:var(--page-white)}
.page-spread{position:absolute;left:698px;top:430px;width:402px;height:186px;
  background:linear-gradient(180deg,var(--page-white) 0%,var(--page-grey) 100%)}

.spine{position:absolute;left:600px;top:290px;transform-origin:0 0;transform:rotate(90deg) translateY(-50%);font-size:12px;letter-spacing:0.04em;white-space:nowrap}

.badge{display:flex;align-items:center;gap:6px;transform:translateX(-50%)}
.badge-dot{width:16px;height:16px;border-radius:50%;background:var(--badge-dark)}
.badge-name{font-size:12px;letter-spacing:0.05em;color:var(--ink-white);white-space:nowrap}

.barcode-box{position:absolute;left:438px;top:664px;width:136px;height:82px;background:var(--barcode-cyan);
  display:flex;align-items:center;justify-content:center;font-size:13px;letter-spacing:0.03em}

.author{font-family:"Lato",sans-serif;font-size:24px;letter-spacing:0.03em;color:var(--author-blue)}
</style>
</head>
<body>
<main class="cover">

  <section class="back">
    <h2 class="abs center-x title-line" style="left:297px;top:88px">BILL TRACKER</h2>
    <div class="rule" style="left:200px;top:128px;width:86px"></div>
    <div class="rule" style="left:317px;top:128px;width:74px"></div>
    <div class="abs center-x amp" style="left:299px;top:114px;font-size:30px">&amp;</div>
    <h2 class="abs center-x title-line" style="left:299px;top:148px">PASSWORD LOG</h2>
    <p class="abs center-x caps" style="left:299px;top:183px;font-size:16px">over 100 pages</p>

    <div class="page-thumb" style="left:114px;top:214px" role="img" aria-label="Bill tracker page preview"></div>
    <p class="abs center-x caps feature" style="left:298px;top:240px">Track Payments up to 8 Years</p>

    <div class="page-thumb" style="left:114px;top:301px" role="img" aria-label="Contacts page preview"></div>
    <p class="abs center-x caps feature" style="left:298px;top:326px">Save Passwords and Contacts</p>

    <div class="page-thumb" style="left:114px;top:386px" role="img" aria-label="Password log page preview"></div>
    <p class="abs center-x caps feature" style="left:299px;top:410px">dates from 20 <sup style="font-size:7px">* *</sup> to &nbsp;20 <sup style="font-size:7px">* *</sup></p>

    <p class="abs center-x caps thanks" style="left:299px;top:499px">
      Thank you for choosing ‘Bill Tracker &amp; Password Log’.<br>
      Please leave a review on Shopvale if you find it helpful in your Life.<br>
      This will help us to produce more high quality content.<br>
      Thank You
    </p>

    <div class="abs badge" style="left:299px;top:586px">
      <span class="badge-dot"></span><span class="badge-name">ELAN HARTWELL</span>
    </div>

    <div class="barcode-box">BARCODE</div>
  </section>

  <p class="spine">BILL TRACKER &amp; PASSWORD LOG</p>

  <section class="front">
    <div class="abs badge" style="left:898px;top:66px">
      <span class="badge-dot" style="width:18px;height:18px"></span><span class="badge-name" style="font-size:13px">ELAN HARTWELL</span>
    </div>

    <h1 class="abs center-x title-line" style="left:898px;top:124px">BILL TRACKER</h1>
    <div class="rule" style="left:731px;top:192px;width:141px"></div>
    <div class="rule" style="left:932px;top:192px;width:138px"></div>
    <div class="abs center-x amp" style="left:906px;top:172px;font-size:46px">&amp;</div>
    <h1 class="abs center-x title-line" style="left:897px;top:217px">PASSWORD LOG</h1>

    <p class="abs center-x caps feature" style="left:772px;top:359px">Save Passwords and Contacts</p>
    <p class="abs center-x caps feature" style="left:1024px;top:359px">Track Payments up to 8 Years</p>
    <p class="abs center-x caps" style="left:899px;top:403px;font-size:16px">over 100 pages</p>

    <div class="page-spread" role="img" aria-label="Three fanned interior page previews: password log, bill tracker and contacts tables"></div>

    <p class="abs center-x caps" style="left:899px;top:624px;font-size:16px">from 20 <sup style="font-size:8px">* *</sup> to &nbsp;20 <sup style="font-size:8px">* *</sup></p>

    <p class="abs center-x author" style="left:894px;top:690px">ELAN HARTWELL</p>
  </section>

</main>
</body>
</html>
```